Quarveling stickers design for our main topics (for example: agile and Kanban)

We are looking for sticker design, that will reflect our cooperate identity and can be used for the different topics in our company. We would like to start with our Agile Coaching Offers with a Kanban Sticker saying "stop starting, start finishing", A bad example can be find in the file upload ;)
Check out our homepage to get a feeling for the cooperate identity (www.quarveling.ch)

Target Market(s)

Customers and trainees from our trainings

Industry/Entity Type

Consulting

Colors
0355a3
fbed22

Requirements
Must have
• a cool design thats fits to our customer design
the 2 lines can be changed for future stickers ... like in the example "stop starting, start finishing" and "we show you how"
Nice to have
• -
Should not have
• -

```html
<!DOCTYPE html>
<html lang="en">
<head>
<meta charset="utf-8">
<title>Quarveling Kanban Stickers</title>
<link rel="stylesheet" href="https://fonts.googleapis.com/css2?family=Roboto:ital,wght@0,400;1,400;1,500&family=Roboto+Condensed:wght@700&display=swap">
<style>
  :root {
    --brand-blue: #0a37e8;
    --brand-yellow: #f9f69c;
    --sticker-white: #ffffff;
    --ink: #1c1c1c;
    --backdrop: #efebe4;
  }
  * { margin: 0; padding: 0; box-sizing: border-box; }
  html, body {
    width: 1200px;
    height: 994px;
    overflow: hidden;
    background: var(--backdrop);
  }
  .sheet {
    position: relative;
    width: 1200px;
    height: 994px;
  }
  .sticker {
    position: absolute;
    left: 177px;
    width: 837px;
    height: 218px;
    background: var(--brand-blue);
    border-radius: 14px;
    overflow: hidden;
    box-shadow: 2px 4px 6px rgba(0, 0, 0, 0.35);
  }
  .sticker--flag   { top: 113px; }
  .sticker--arrows { top: 366px; }
  .sticker--target { top: 615px; }

  .corner-curve {
    position: absolute;
    inset: 0;
    width: 837px;
    height: 218px;
  }
  .corner-curve .edge { fill: var(--brand-yellow); }
  .corner-curve .field { fill: var(--sticker-white); }

  .headline {
    position: absolute;
    font-family: "Roboto", sans-serif;
    font-weight: 400;
    font-size: 52px;
    line-height: 1;
    color: var(--sticker-white);
    white-space: nowrap;
  }
  .ribbon {
    position: absolute;
    width: 367px;
    height: 72px;
  }
  .ribbon svg {
    position: absolute;
    inset: 0;
    width: 100%;
    height: 100%;
  }
  .ribbon svg polygon { fill: var(--brand-yellow); }
  .ribbon-text {
    position: absolute;
    left: 20px;
    top: 8px;
    font-family: "Roboto Condensed", sans-serif;
    font-weight: 700;
    font-size: 52px;
    line-height: 1;
    color: var(--brand-blue);
    white-space: nowrap;
  }

  .icon-figure {
    position: absolute;
    background: var(--brand-yellow);
    border-radius: 10px;
  }
  .arrow-row {
    position: absolute;
    left: 28px;
    top: 45px;
    width: 102px;
    height: 31px;
  }
  .arrow-row polygon { fill: var(--brand-yellow); }
  .flag-pole {
    position: absolute;
    left: 141px;
    top: 168px;
    width: 7px;
    height: 50px;
    background: var(--brand-yellow);
  }

  .tagline {
    position: absolute;
    font-family: "Roboto", sans-serif;
    font-style: italic;
    font-weight: 400;
    font-size: 25px;
    line-height: 1;
    color: var(--ink);
    white-space: nowrap;
  }
  .tagline--medium { font-weight: 500; font-size: 22px; }

  .web-address {
    position: absolute;
    left: 160px;
    top: 171px;
    font-family: "Roboto", sans-serif;
    font-style: italic;
    font-weight: 500;
    font-size: 23px;
    line-height: 1;
    color: var(--sticker-white);
    white-space: nowrap;
  }

  .company {
    position: absolute;
    display: flex;
    align-items: center;
    gap: 10px;
  }
  .company-mark {
    width: 36px;
    height: 36px;
    background: var(--brand-blue);
  }
  .company-name {
    font-family: "Roboto", sans-serif;
    font-weight: 400;
    font-size: 25px;
    line-height: 1;
    color: var(--ink);
    white-space: nowrap;
  }
</style>
</head>
<body>
<main class="sheet">

  <section class="sticker sticker--flag">
    <svg class="corner-curve" viewBox="0 0 837 218" aria-hidden="true">
      <path class="edge" d="M500,218 C545,100 690,22 837,14 L837,218 Z"/>
      <path class="field" d="M519,218 C560,110 700,40 837,31 L837,218 Z"/>
    </svg>
    <div class="icon-figure" role="img" aria-label="Icon of a person planting a finish flag" style="left:31px; top:53px; width:107px; height:119px;"></div>
    <p class="headline" style="left:163px; top:32px;">Stop starting,</p>
    <div class="ribbon" style="left:150px; top:101px;">
      <svg viewBox="0 0 367 72" preserveAspectRatio="none" aria-hidden="true"><polygon points="0,0 367,0 337,36 367,72 0,72"/></svg>
      <span class="ribbon-text">Start finishing</span>
    </div>
    <p class="tagline" style="left:700px; top:88px;">kanban@</p>
    <div class="company" style="left:620px; top:114px;">
      <span class="company-mark"></span>
      <span class="company-name">quarveling ag</span>
    </div>
  </section>

  <section class="sticker sticker--arrows">
    <svg class="corner-curve" viewBox="0 0 837 218" aria-hidden="true">
      <path class="edge" d="M500,218 C545,100 690,20 837,13 L837,218 Z"/>
      <path class="field" d="M519,218 C560,110 700,38 837,30 L837,218 Z"/>
    </svg>
    <svg class="arrow-row" viewBox="0 0 102 31" aria-hidden="true">
      <polygon points="0,0 24,15.5 0,31"/>
      <polygon points="38,0 62,15.5 38,31"/>
      <polygon points="76,0 100,15.5 76,31"/>
    </svg>
    <p class="headline" style="left:155px; top:28px;">Stop starting,</p>
    <div class="ribbon" style="left:141px; top:98px;">
      <svg viewBox="0 0 367 72" preserveAspectRatio="none" aria-hidden="true"><polygon points="0,0 367,0 337,36 367,72 0,72"/></svg>
      <span class="ribbon-text">Start finishing</span>
    </div>
    <span class="flag-pole" aria-hidden="true"></span>
    <p class="tagline tagline--medium" style="left:632px; top:105px;">We show you how</p>
    <div class="company" style="left:620px; top:131px;">
      <span class="company-mark"></span>
      <span class="company-name">quarveling ag</span>
    </div>
  </section>

  <section class="sticker sticker--target">
    <svg class="corner-curve" viewBox="0 0 837 218" aria-hidden="true">
      <path class="edge" d="M566,218 C605,118 710,58 837,50 L837,218 Z"/>
      <path class="field" d="M583,218 C620,130 720,75 837,67 L837,218 Z"/>
    </svg>
    <div class="icon-figure" role="img" aria-label="Icon of an arrow hitting a target" style="left:14px; top:59px; width:108px; height:96px; border-radius:50%;"></div>
    <p class="headline" style="left:164px; top:15px;">Stop starting,</p>
    <div class="ribbon" style="left:150px; top:83px;">
      <svg viewBox="0 0 367 72" preserveAspectRatio="none" aria-hidden="true"><polygon points="0,0 367,0 337,36 367,72 0,72"/></svg>
      <span class="ribbon-text">Start finishing</span>
    </div>
    <p class="web-address">www.quarveling.ch/kanban-coaching</p>
    <div class="company" style="left:640px; top:140px;">
      <span class="company-mark"></span>
      <span class="company-name">quarveling ag</span>
    </div>
  </section>

</main>
</body>
</html>
```